Cedar Hall letterhead

We changed our name and logo now need letterhead.
3-4/72 Harlow Street Linden Vale 2790
www.cedarhall.org.au
info@cedarhall.org.au
ph: 01 5550 7342

At this stage, we are preferencing Design #: 5398880 and Design #5401338

```html
<!DOCTYPE html>
<html lang="en">
<head>
<meta charset="utf-8">
<title>Cedar Hall Letterhead and Business Card</title>
<link href="https://fonts.googleapis.com/css2?family=Open+Sans:wght@400;600&family=Oswald:wght@300;400&display=swap" rel="stylesheet">
<style>
  :root {
    --backdrop: #e6e8ea;
    --paper: #ffffff;
    --ink: #1f1f1f;
    --ink-soft: #3a3a3a;
    --brand: #8596a6;
    --brand-dark: #5f7080;
    --rule: #9a9a9a;
  }
  * { box-sizing: border-box; margin: 0; padding: 0; }
  html, body { width: 1200px; height: 1000px; overflow: hidden; }
  body { background: var(--backdrop); font-family: "Open Sans", Arial, sans-serif; color: var(--ink); position: relative; }

  .letterhead {
    position: absolute; left: 90px; top: 45px; width: 640px; height: 905px;
    background: var(--paper); box-shadow: 0 2px 10px rgba(0,0,0,.12);
  }
  .brand { position: absolute; display: flex; align-items: center; gap: 12px; }
  .brand-dot { border-radius: 50%; background: var(--brand); flex: none; }
  .brand-name { color: var(--brand-dark); font-weight: 400; white-space: nowrap; }

  .letterhead > .brand { left: 70px; top: 70px; }
  .letterhead > .brand .brand-dot { width: 70px; height: 70px; }
  .letterhead > .brand .brand-name { font-size: 22px; }

  .letter-body { position: absolute; left: 110px; top: 205px; width: 440px; }
  .salutation { font-size: 21px; font-weight: 400; margin-bottom: 10px; }
  .letter-body p { font-size: 11.5px; line-height: 1.48; color: var(--ink-soft); margin-bottom: 14px; }

  .footer-band { position: absolute; left: 60px; right: 60px; top: 705px; height: 70px; }
  .footer-band .brand { left: 8px; top: 14px; }
  .footer-band .brand-dot { width: 38px; height: 38px; }
  .footer-divider { position: absolute; left: 58px; top: 8px; width: 1px; height: 52px; background: var(--rule); }
  .footer-contact { position: absolute; left: 70px; top: 12px; font-family: "Oswald", "Arial Narrow", sans-serif; font-weight: 300; font-size: 9.5px; letter-spacing: .6px; line-height: 1.45; text-transform: uppercase; white-space: nowrap; }
  .footer-rule { position: absolute; left: 0; right: 0; top: 62px; height: 1px; background: var(--rule); }
  .signature { position: absolute; right: 20px; top: 18px; width: 120px; height: 34px; background: linear-gradient(90deg, #f1f1f1, #e6e6e6); border-radius: 3px; }

  .site-rule { position: absolute; left: 60px; right: 60px; top: 835px; height: 1px; background: var(--rule); }
  .site-url { position: absolute; right: 60px; top: 842px; font-family: "Oswald", "Arial Narrow", sans-serif; font-weight: 300; font-size: 10px; letter-spacing: .7px; text-transform: uppercase; }

  .business-card {
    position: absolute; left: 800px; top: 560px; width: 340px; height: 200px;
    background: var(--paper); box-shadow: 0 2px 10px rgba(0,0,0,.12);
  }
  .card-brand { position: absolute; left: 22px; top: 34px; width: 74px; display: flex; flex-direction: column; align-items: center; gap: 14px; }
  .card-brand .brand-dot { width: 62px; height: 62px; }
  .card-brand .brand-name { font-size: 13px; }
  .card-details { position: absolute; left: 130px; top: 30px; font-family: "Oswald", "Arial Narrow", sans-serif; font-weight: 300; text-transform: uppercase; letter-spacing: .6px; white-space: nowrap; }
  .card-name { font-size: 19px; font-weight: 400; }
  .card-title { font-size: 9px; margin-bottom: 14px; }
  .card-line { font-size: 10px; line-height: 1.45; }
  .card-gap { height: 12px; }
</style>
</head>
<body>

<section class="letterhead" aria-label="Cedar Hall letterhead">
  <div class="brand">
    <span class="brand-dot"></span>
    <span class="brand-name">Cedar Hall</span>
  </div>

  <div class="letter-body">
    <h1 class="salutation">Dear Mr. Lorem,</h1>
    <p>Lorem ipsum dolor sit amet, consectetur adipiscing elit. Pellentesque ac dolor leo est pellentesque ornare ut vitae nulla. Mauris in eros nunc. Curabitur in odio aliquet bibendum est in, facilisis mi. Suspendisse potenti. Morbi fermentum pretium felis, ac scelerisque sapien tempus ut. Quisque vulputate mollis ex, in lacinia urna ultrices a. Sed dapibus imperdiet varius. Etiam magna elit, pulvinar vel sapien quis, convallis euismod turpis. Nam vitae ipsum sit amet justo sodales tincidunt. Class aptent taciti sociosqu ad litora torquent per conubia nostra, per inceptos himenaeos. Praesent nec risus nulla. Etiam justo ligula, condimentum vitae varius at, venenatis ac tellus. Quisque dignissim ac ante a cursus. Curabitur vitae mollis augue. Mauris non massa blandit, pharetra enim ac, egestas dui. Integer non nisl libero.</p>
    <p>Vestibulum eget egestas ipsum, nec convallis libero. Duis scelerisque et enim sit amet volutpat. Nullam sit amet est lorem. Vivamus sit amet iaculis libero. Suspendisse in semper nisl, non pharetra est. Curabitur sed euismod massa. Vivamus rutrum nunc sit amet lobortis vehicula. Aenean commodo convallis nibh in feugiat. Cras nec est sodales, scelerisque libero vel, fermentum arcu.</p>
    <p>Vestibulum eget egestas ipsum, nec convallis libero. Duis scelerisque et enim sit amet volutpat. Nullam sit amet est lorem. Vivamus sit amet iaculis libero. Suspendisse in semper nisl, non pharetra est. Curabitur sed euismod massa. Vivamus rutrum nunc sit amet lobortis vehicula. Aenean commodo convallis nibh in feugiat. Cras nec est sodales, scelerisque libero vel, fermentum arcu.</p>
  </div>

  <div class="footer-band">
    <div class="brand"><span class="brand-dot"></span></div>
    <span class="footer-divider"></span>
    <div class="footer-contact">
      <div>01 5550 7342</div>
      <div>info@cedarhall.org.au</div>
      <div>3-4/72 Harlow Street, Linden Vale 2790</div>
    </div>
    <div class="signature" role="img" aria-label="Handwritten signature of the sender"></div>
    <span class="footer-rule"></span>
  </div>

  <span class="site-rule"></span>
  <div class="site-url">www.cedarhall.org.au</div>
</section>

<section class="business-card" aria-label="Cedar Hall business card">
  <div class="card-brand">
    <span class="brand-dot"></span>
    <span class="brand-name">Cedar Hall</span>
  </div>
  <div class="card-details">
    <div class="card-name">Name Surname</div>
    <div class="card-title">Title</div>
    <div class="card-line">(000) 0000 0000</div>
    <div class="card-line">email@email.com</div>
    <div class="card-gap"></div>
    <div class="card-line">social.cedarhall.org.au/name</div>
    <div class="card-line">posts.cedarhall.org.au/name</div>
  </div>
</section>

</body>
</html>
```